Bref créative
Business card and stationary design for engineering and manufacturing company
Valdorkin Engineering Inc. - (Below) A Pioneer in the Signal Mast Trade Since 1983
Professional
Mark Pellow
2719 North 58th Avenue
Yankton, SD 57391
info@valdorkinengineering.example
www.valdorkinengineering.example
I need a business card that I can edit names and email addresses for multiple employees. Check out my logo upload and our website. The stationary is general and will be non-specific to a contact name.

```html
<!DOCTYPE html>
<html lang="en">
<head>
<meta charset="utf-8">
<title>Valdorkin Engineering Inc. – Business Card</title>
<link rel="stylesheet" href="https://fonts.googleapis.com/css2?family=Open+Sans:wght@400;600&family=Roboto+Condensed:wght@700&display=swap">
<style>
  :root {
    --backdrop: #d9d9d6;
    --card-white: #fbfbfb;
    --band-dark: #333333;
    --ink-dark: #2a2a2a;
    --accent-orange: #f26f21;
    --text-light: #f2f2f2;
    --icon-bg: #f2f2f2;
  }
  * { margin: 0; padding: 0; box-sizing: border-box; }
  html, body {
    width: 1200px; height: 902px; overflow: hidden;
    background: var(--backdrop);
  }
  .canvas {
    width: 1200px; height: 902px;
    display: flex; align-items: center; justify-content: center;
  }
  .business-card {
    position: relative;
    width: 900px; height: 514px;
    background: var(--card-white);
    box-shadow: 0 14px 36px rgba(0,0,0,0.18);
    overflow: hidden;
  }
  .brand-lockup {
    position: absolute;
    top: 78px; left: 0; right: 0;
    display: flex; align-items: center; justify-content: center;
    gap: 22px;
  }
  .brand-square {
    width: 62px; height: 62px;
    background: var(--accent-orange);
  }
  .brand-name {
    font-family: "Roboto Condensed", "Arial Narrow", sans-serif;
    font-weight: 700;
    font-size: 46px;
    line-height: 1;
    letter-spacing: 0.5px;
    color: var(--ink-dark);
    text-transform: uppercase;
  }
  .info-band {
    position: absolute;
    left: 0; right: 0;
    top: 228px; height: 236px;
    background: var(--band-dark);
  }
  .name-tab {
    position: absolute;
    left: 0; top: 150px;
    width: 12px; height: 40px;
    background: var(--accent-orange);
  }
  .employee-name {
    position: absolute;
    left: 34px; top: 158px;
    font-family: "Open Sans", Arial, sans-serif;
    font-weight: 600;
    font-size: 20px;
    color: var(--text-light);
  }
  .contact-list {
    position: absolute;
    left: 545px; top: 18px;
    list-style: none;
    font-family: "Open Sans", Arial, sans-serif;
    font-size: 15px;
    color: var(--text-light);
  }
  .contact-item {
    display: flex; align-items: flex-start; gap: 10px;
    line-height: 19px;
    margin-bottom: 6px;
  }
  .contact-icon {
    flex: none;
    width: 18px; height: 18px;
    margin-top: 1px;
  }
  .contact-icon.spacer { visibility: hidden; }
</style>
</head>
<body>
<div class="canvas">
  <div class="business-card">
    <div class="brand-lockup">
      <div class="brand-square"></div>
      <div class="brand-name">Valdorkin Engineering Inc.</div>
    </div>

    <div class="info-band">
      <div class="name-tab"></div>
      <div class="employee-name">Mark Pellow</div>

      <ul class="contact-list">
        <li class="contact-item">
          <svg class="contact-icon" viewBox="0 0 18 18" aria-hidden="true">
            <circle cx="9" cy="9" r="9" fill="var(--icon-bg)"/>
            <path d="M9 4a3 3 0 0 1 3 3c0 2.3-3 6-3 6s-3-3.7-3-6a3 3 0 0 1 3-3z" fill="var(--band-dark)"/>
            <circle cx="9" cy="7" r="1.1" fill="var(--icon-bg)"/>
          </svg>
          <span>2719 North 58th Avenue<br>Yankton, SD 57391</span>
        </li>
        <li class="contact-item">
          <svg class="contact-icon" viewBox="0 0 18 18" aria-hidden="true">
            <circle cx="9" cy="9" r="9" fill="var(--icon-bg)"/>
            <path d="M6 4.5l2 2.2-1 1.3a6 6 0 0 0 3 3l1.3-1 2.2 2-1.2 1.5C9.5 13.5 4.5 8.5 4.5 5.7z" fill="var(--band-dark)"/>
          </svg>
          <span>800-555-0142</span>
        </li>
        <li class="contact-item">
          <svg class="contact-icon" viewBox="0 0 18 18" aria-hidden="true">
            <circle cx="9" cy="9" r="9" fill="var(--icon-bg)"/>
            <path d="M6 4.5l2 2.2-1 1.3a6 6 0 0 0 3 3l1.3-1 2.2 2-1.2 1.5C9.5 13.5 4.5 8.5 4.5 5.7z" fill="var(--band-dark)"/>
          </svg>
          <span>605-555-0187</span>
        </li>
        <li class="contact-item">
          <svg class="contact-icon" viewBox="0 0 18 18" aria-hidden="true">
            <circle cx="9" cy="9" r="9" fill="var(--icon-bg)"/>
            <rect x="5" y="7" width="8" height="5" fill="var(--band-dark)"/>
            <rect x="6.5" y="4.5" width="5" height="3" fill="none" stroke="var(--band-dark)" stroke-width="1"/>
          </svg>
          <span>605-555-0163</span>
        </li>
        <li class="contact-item">
          <svg class="contact-icon" viewBox="0 0 18 18" aria-hidden="true">
            <circle cx="9" cy="9" r="9" fill="var(--icon-bg)"/>
            <rect x="4.5" y="6" width="9" height="6.5" fill="var(--band-dark)"/>
            <path d="M4.5 6l4.5 3.6L13.5 6" fill="none" stroke="var(--icon-bg)" stroke-width="0.9"/>
          </svg>
          <span>info@valdorkinengineering.example</span>
        </li>
        <li class="contact-item">
          <svg class="contact-icon" viewBox="0 0 18 18" aria-hidden="true">
            <circle cx="9" cy="9" r="9" fill="var(--icon-bg)"/>
            <circle cx="9" cy="9" r="4.5" fill="none" stroke="var(--band-dark)" stroke-width="1.1"/>
            <ellipse cx="9" cy="9" rx="2" ry="4.5" fill="none" stroke="var(--band-dark)" stroke-width="1"/>
            <line x1="4.5" y1="9" x2="13.5" y2="9" stroke="var(--band-dark)" stroke-width="1"/>
          </svg>
          <span>www.valdorkinengineering.example</span>
        </li>
      </ul>
    </div>
  </div>
</div>
</body>
</html>
```